Retractable Banner Design for Retail Shopping Event

I need a design for a 33” by 86” retractable banner. It should have my logo at the top (the largest element of the design) and the banner should also include my website and Instagram handle:
www.verikamode.com
@verikamode
I have included product pictures in the brief that can be used. I also included different versions of my logo file, including AI. I need the file to be ready to upload to my printer.
My store is an upscale women’s boutique. I am also attaching designs I have selected in the past to give an idea of my aesthetic.

```html
<!DOCTYPE html>
<html lang="en">
<head>
<meta charset="utf-8">
<title>Verika Mode – Sip &amp; Shop Banner</title>
<link rel="stylesheet" href="https://fonts.googleapis.com/css2?family=Abril+Fatface&family=Montserrat:wght@400;500;700&family=Norican&display=swap">
<style>
  :root {
    --page: #f4f4f6;
    --blush: #f1dcd8;
    --blush-light: #f8eeec;
    --blush-deep: #ecd2cd;
    --ink: #5b5b5d;
    --line: #ffffff;
    --bag: #d9c2b4;
    --gold: #d5a85c;
    --tray: #cdb58a;
    --slipper: #b79aa6;
  }
  * { margin: 0; padding: 0; box-sizing: border-box; }
  html, body { width: 1200px; height: 2326px; overflow: hidden; background: var(--page); }
  .banner {
    position: absolute; left: 190px; top: 94px; width: 820px; height: 2137px;
    background: linear-gradient(160deg, var(--blush-deep) 0%, var(--blush) 45%, var(--blush) 100%);
    overflow: hidden; font-family: "Montserrat", sans-serif; color: var(--ink);
  }
  .backdrop { position: absolute; inset: 0; }
  .brand {
    position: absolute; left: 67px; top: 74px; width: 686px; height: 237px;
    display: flex; flex-direction: column; align-items: center; justify-content: center;
  }
  .brand-name {
    font-family: "Abril Fatface", serif; font-size: 92px; letter-spacing: 4px; line-height: 1;
  }
  .brand-sub {
    font-family: "Abril Fatface", serif; font-size: 40px; letter-spacing: 14px; margin-top: 16px; line-height: 1;
  }
  .event-title {
    position: absolute; left: 90px; top: 380px;
    font-family: "Norican", cursive; font-size: 128px; line-height: 1;
  }
  .invite { position: absolute; left: 90px; top: 580px; }
  .invite-head { font-size: 98px; font-weight: 500; line-height: 0.92; letter-spacing: 1px; }
  .perks { list-style: none; margin-top: 20px; }
  .perks li { font-size: 46px; line-height: 57px; display: flex; align-items: center; gap: 16px; }
  .perks svg { width: 26px; height: 26px; }
  .product { position: absolute; }
  .product-bag { left: 425px; top: 624px; width: 400px; height: 603px; border-radius: 40px 0 0 30px;
    background: linear-gradient(120deg, #efe2da, var(--bag) 60%, #c9ad9c); }
  .product-earrings { left: 70px; top: 986px; width: 249px; height: 231px; border-radius: 50%;
    background: radial-gradient(circle, #e7c98c 0%, var(--gold) 45%, rgba(213,168,92,0) 72%); }
  .product-tray { left: 188px; top: 1125px; width: 438px; height: 296px; border-radius: 50%;
    background: radial-gradient(ellipse, #d9c7a0 0%, var(--tray) 55%, #8f7a58 100%); }
  .product-slippers { left: 0; top: 1427px; width: 294px; height: 287px; border-radius: 0 50% 45% 0;
    background: linear-gradient(140deg, #e8c8c4, var(--slipper) 70%, #8c7483); }
  .teaser {
    position: absolute; right: 63px; top: 1614px; text-align: right;
    font-size: 39px; line-height: 51px;
  }
  .contact { position: absolute; right: 63px; top: 1935px; text-align: right; }
  .contact-row { display: flex; align-items: center; justify-content: flex-end; gap: 22px;
    font-size: 46px; font-weight: 700; line-height: 66px; }
  .contact-row svg { width: 30px; height: 30px; }
</style>
</head>
<body>
<main class="banner">
  <svg class="backdrop" viewBox="0 0 820 2137" width="820" height="2137" aria-hidden="true">
    <defs>
      <linearGradient id="sheen" x1="0" y1="0" x2="1" y2="1">
        <stop offset="0" stop-color="#fbf3f2" stop-opacity="0.9"/>
        <stop offset="1" stop-color="#fbf3f2" stop-opacity="0"/>
      </linearGradient>
    </defs>
    <polygon points="820,0 820,690 120,1330 0,1330 0,0" fill="url(#sheen)"/>
    <polygon points="820,1340 820,1590 640,1590" fill="#f6e6e3"/>
    <line x1="0" y1="466" x2="360" y2="736" stroke="var(--line)" stroke-width="3" opacity="0.8"/>
    <line x1="0" y1="2051" x2="820" y2="1227" stroke="var(--line)" stroke-width="5"/>
    <rect x="67" y="74" width="686" height="237" fill="none" stroke="var(--ink)" stroke-width="4"/>
  </svg>

  <header class="brand">
    <span class="brand-name">VERIKA</span>
    <span class="brand-sub">MODE</span>
  </header>

  <h1 class="event-title">Sip &amp; Shop</h1>

  <section class="invite">
    <h2 class="invite-head">COME<br>ENJOY</h2>
    <ul class="perks">
      <li><svg viewBox="0 0 20 20"><path d="M3 10l5 6 9-13" fill="none" stroke="currentColor" stroke-width="2.5"/></svg>SIPS</li>
      <li><svg viewBox="0 0 20 20"><path d="M3 10l5 6 9-13" fill="none" stroke="currentColor" stroke-width="2.5"/></svg>SNACKS</li>
      <li><svg viewBox="0 0 20 20"><path d="M3 10l5 6 9-13" fill="none" stroke="currentColor" stroke-width="2.5"/></svg>SHOPPING</li>
    </ul>
  </section>

  <div class="product product-bag" role="img" aria-label="Blush satin tote bag with a beaded teal serpent motif"></div>
  <div class="product product-earrings" role="img" aria-label="Pair of gold quatrefoil stud earrings with crystals"></div>
  <div class="product product-tray" role="img" aria-label="Round leopard print decorative tray"></div>
  <div class="product product-slippers" role="img" aria-label="Mauve slippers with pink pom-pom straps"></div>

  <p class="teaser">Be the first to<br>preview our new<br>winter collection<br>and get an early<br>start on your<br>holiday gifting</p>

  <div class="contact">
    <div class="contact-row">www.verikamode.com
      <svg viewBox="0 0 20 20"><circle cx="10" cy="10" r="8" fill="none" stroke="currentColor" stroke-width="2"/><path d="M2 10h16M10 2c-4 4-4 12 0 16M10 2c4 4 4 12 0 16" fill="none" stroke="currentColor" stroke-width="1.6"/></svg>
    </div>
    <div class="contact-row">@verikamode
      <svg viewBox="0 0 20 20"><rect x="2" y="2" width="16" height="16" rx="3" fill="none" stroke="currentColor" stroke-width="2"/></svg>
    </div>
  </div>
</main>
</body>
</html>
```